Album cover art for Christmas Holiday single of “Bright Winter Lantern (Das Schneelicht)” Artist alias is “Dorran Kesley” Attached an image that could be incorporated for the album art. This will be a surprise release for my fans for Dec 1. I’m a Saxophonist and will have this art visible for stream via Melodrop, Wavetrove, ClipHarbor, brimsell, etc. I’d love a design that is cozy, jazzy, and traditional. It’s promotional so I’d love my image incorporated in some way.

Target Market(s)

Smooth Jazz lovers, instrumentals, saxophone

Requirements
Must have
• Must incorporate the attached picture
Nice to have
• Color schemes and branding consistent with my website http://dorrank-sax.example

```html
<!DOCTYPE html>
<html lang="en">
<head>
<meta charset="utf-8">
<title>Dorran Kesley – Bright Winter Lantern</title>
<link rel="stylesheet" href="https://fonts.googleapis.com/css2?family=Alegreya:wght@400;700&family=Montserrat:wght@600&display=swap">
<style>
  :root {
    --crimson: #a20d3c;
    --badge: #a50f3e;
    --violet: #3f1d6b;
    --white: #ffffff;
    --night: #2a1d2e;
    --dusk: #5a3f4a;
    --glow-gold: #e8c77a;
    --glow-warm: #b98a55;
    --facade: #c9b4b6;
    --ornament: #b3123f;
    --coat: #5b524f;
    --coat-dark: #3a3436;
    --coat-light: #8a7f86;
  }
  * { margin: 0; padding: 0; box-sizing: border-box; }
  html, body { width: 1200px; height: 1200px; overflow: hidden; background: var(--night); }
  .cover { position: relative; width: 1200px; height: 1200px; overflow: hidden; }

  .backdrop-photo {
    position: absolute; inset: 0;
    background:
      radial-gradient(circle 128px at 900px 40px, var(--ornament) 0%, var(--ornament) 96%, transparent 100%),
      radial-gradient(ellipse 280px 480px at 580px 500px, var(--glow-gold) 0%, var(--glow-warm) 45%, transparent 78%),
      radial-gradient(ellipse 300px 520px at 1100px 560px, var(--facade) 0%, transparent 72%),
      linear-gradient(160deg, var(--dusk) 0%, var(--night) 55%, #3a2a36 100%);
  }

  .artist-photo {
    position: absolute; left: 0; top: 135px; width: 490px; height: 1065px;
    border-radius: 180px 180px 0 0;
    background:
      radial-gradient(ellipse 160px 220px at 60px 420px, rgba(170,140,255,0.55) 0%, transparent 80%),
      linear-gradient(180deg, var(--coat-light) 0%, var(--coat) 35%, var(--coat-dark) 100%);
  }

  .gift-badge {
    position: absolute; left: 932px; top: 34px;
    width: 232px; height: 232px; border-radius: 50%;
    background: var(--badge);
    display: flex; flex-direction: column; align-items: center; justify-content: center;
    color: var(--white);
    font-family: "Montserrat", sans-serif; font-weight: 600;
    text-align: center; line-height: 1.05;
  }
  .gift-badge .gift-label { font-size: 38px; letter-spacing: 1px; }
  .gift-badge .gift-name { font-size: 30px; letter-spacing: 0.5px; margin-top: 8px; }

  .artist-band {
    position: absolute; left: 424px; top: 880px; width: 776px; height: 112px;
    background: var(--violet);
    display: flex; align-items: center; padding-left: 60px;
  }
  .artist-name {
    font-family: "Montserrat", sans-serif; font-weight: 600;
    font-size: 64px; letter-spacing: 3px; color: var(--white); line-height: 1;
  }

  .title-band {
    position: absolute; left: 0; top: 992px; width: 1200px; height: 208px;
    background: var(--crimson);
  }
  .track-title {
    position: absolute; left: 490px; top: 28px;
    font-family: "Alegreya", serif; font-weight: 700;
    font-size: 64px; color: var(--white); line-height: 1; white-space: nowrap;
  }
  .track-subtitle {
    position: absolute; left: 490px; top: 110px;
    font-family: "Alegreya", serif; font-weight: 400;
    font-size: 54px; color: var(--white); line-height: 1; white-space: nowrap;
  }
</style>
</head>
<body>
  <main class="cover">
    <div class="backdrop-photo" role="img" aria-label="Blurred evening scene with a large lit Christmas tree, a red starred ornament and a festive white building"></div>

    <div class="title-band">
      <h2 class="track-title">Bright Winter Lantern</h2>
      <p class="track-subtitle">(Das Schneelicht)</p>
    </div>

    <div class="artist-band">
      <h1 class="artist-name">DORRAN KESLEY</h1>
    </div>

    <div class="artist-photo" role="img" aria-label="Photo of the saxophonist in a flat cap, plaid scarf and grey coat, smiling and holding an alto saxophone"></div>

    <div class="gift-badge">
      <span class="gift-label">GIFT BY</span>
      <span class="gift-name">DORRAN K.</span>
    </div>
  </main>
</body>
</html>
```